Design Creative Banner or Gif Ads. 3 Designs To Be Selected

Come up with some creative banner ads for stonewell.co.nz

*At least 3 different winning banners will be chosen*

Please provide banner ads / gif ads in common google ads / website banner formats.

They can be gif or static but must stand out while still maintaining clear clean text and visuals, with a premium professional feel (please avoid clip art or anything that gives a cheap message).

Please keep in mind that these will likely be small ads so text needs to be large and if there's there a lot of text then use multiple frames/ pages as submit as a gif.

Style
Minimal & clean lines
Architectural or realistic images
Avoid cartoon styles, clipart, or anything that looks cheap

Font
Nexa or Montserrat or similar

Tone
Premium, serious, trustworthy — fits new builds

Colours
Option 1: Deep Navy (trust & quality) & lighter blues and warm grey
Option 2: Open to bright colours to help the ads stand out, such as (but not limited to) bright pink with black, yellow, fluorescent green, provided the messaging is still done professionally.
Our logo is attached (Stone Well Logo)

Display Sizes
Ad specs for file sizes should be file formats like JPEG, GIF, and PNG, with animations limited to a max of 30 seconds or less.
We will need several different ad sizes provided for each of the 3 selected winning designs.

• Medium Rectangle: 300 × 250 pixels
• Leaderboard: 728 × 90 pixels
• Desktop Banner ad image: (640x360 pixels)
• Desktop Banner ad image 2: (300x600 pixels)
• Possibly one or two other sizes

Flexibility to be creative
The ad text, words, upper/lower case, layout, colour, theme, and images can be adjusted to how you think it will look best. The follow example ads are just examples of what we are after but we are keen to see what you can create.

Recommendations at this point:
1. Avoid text heavy
2. Looking for more Gif ads
3. Imaging: if possible use real stock photo's rather than AI

Themes:

1
Building Soon? Start Here
Free Build Planning Pack:
✓ Build Cost Calculator
✓ Hidden Cost Checklist
✓ Builder Comparison Guide
Build With Confidence
Download Free

2
Before You Choose A Builder
Compare Price, Scope, Risk & Value
Avoid Costly Mistakes
Choose The Right Builder With Confidence
Download The Free Guide

3
Planning A New Build?
Avoid These Common Mistakes:
✗ Hidden Exclusions
✗ Missing Scope
✗ Unrealistic Allowances
✗ Budget Blowouts
Download The Free Guide

4
Before You Buy Land
Know what it could cost to build.
Avoid Costly Building Mistakes
Download Our Free Guides

5
Know Your Build Budget?
• Free Build Cost Calculator
• Hidden Cost Checklist
• Build Planning Tools
Calculate Costs (Download)

Target Market(s)

Landowners looking to build

Industry/Entity Type

Building

Font styles to use
Other font styles liked:
• Nexa or Montserrat or similar

Requirements
Should not have
• Avoid cartoon styles, clipart, or anything that looks cheap

```html
<!DOCTYPE html>
<html lang="en">
<head>
<meta charset="utf-8">
<title>Stone Well – Know Your Build Budget?</title>
<link rel="stylesheet" href="https://fonts.googleapis.com/css2?family=Montserrat:wght@600;700;800&display=swap">
<style>
  :root {
    --navy: #0c2b45;
    --blue: #3a9bcb;
    --paper: #f2f7fb;
    --photo-top: #dfe6ec;
    --photo-bottom: #b9a58e;
  }
  * { margin: 0; padding: 0; box-sizing: border-box; }
  html, body { width: 1200px; height: 2400px; overflow: hidden; }
  body {
    position: relative;
    background: var(--paper);
    font-family: "Montserrat", Arial, sans-serif;
    color: var(--navy);
  }
  .brand-mark {
    position: absolute;
    left: 220px;
    top: 138px;
    width: 150px;
    height: 150px;
    background: var(--navy);
  }
  .brand {
    position: absolute;
    left: 440px;
    top: 158px;
  }
  .brand-name {
    font-size: 82px;
    font-weight: 700;
    letter-spacing: -1px;
    line-height: 1;
    color: var(--navy);
  }
  .brand-tagline {
    margin-top: 18px;
    font-size: 22px;
    font-weight: 700;
    letter-spacing: 0.5px;
    color: var(--blue);
    white-space: nowrap;
  }
  .hero-photo {
    position: absolute;
    left: 0;
    top: 400px;
    width: 1200px;
    height: 780px;
    background: linear-gradient(180deg, var(--photo-top) 0%, var(--photo-top) 45%, var(--photo-bottom) 100%);
    clip-path: polygon(0 0, 100% 0, 100% 580px, 50% 770px, 0 580px);
  }
  .chevron-band {
    position: absolute;
    left: 0;
    top: 0;
    width: 1200px;
    height: 1240px;
  }
  .next-arrows {
    position: absolute;
    left: 996px;
    top: 1328px;
    width: 128px;
    height: 108px;
  }
  .headline {
    position: absolute;
    left: 190px;
    top: 1560px;
    font-size: 160px;
    font-weight: 800;
    line-height: 184px;
    letter-spacing: -2px;
    color: var(--navy);
  }
  .headline .accent { color: var(--blue); }
  .footer-bar {
    position: absolute;
    left: 0;
    bottom: 0;
    width: 1200px;
    height: 40px;
    background: var(--navy);
  }
</style>
</head>
<body>
  <div class="brand-mark" aria-hidden="true"></div>
  <header class="brand">
    <div class="brand-name">Stone Well</div>
    <div class="brand-tagline">COMPARE QUOTES FROM TRUSTED BUILDERS</div>
  </header>

  <div class="hero-photo" role="img" aria-label="Photo of a finished dark-clad gable house beside a timber-framed house under construction on a building site"></div>

  <svg class="chevron-band" viewBox="0 0 1200 1240" aria-hidden="true">
    <polygon points="0,972 600,1160 1200,972 1200,1072 600,1225 0,1072" fill="var(--blue)"/>
  </svg>

  <svg class="next-arrows" viewBox="0 0 128 108" aria-hidden="true">
    <polyline points="10,10 52,54 10,98" fill="none" stroke="var(--blue)" stroke-width="22"/>
    <polyline points="66,10 108,54 66,98" fill="none" stroke="var(--blue)" stroke-width="22"/>
  </svg>

  <h1 class="headline">Know<br>Your Build<br><span class="accent">Budget</span>?</h1>

  <div class="footer-bar"></div>
</body>
</html>
```